New home full landscape package

We have a landscape construction company and have built a new home landscape package and wish to have it on a double sided a5 brochure for us to leave with sales agents. I have attached everything i can think off that would need to be incorporated and am accessible to answer any questions required.

Target Market(s)

new home buyers

Industry/Entity Type

Landscaping

Requirements
Must have
• highlighting $9990 + gst component
• clear directive/ outcome for clients
• 'whats in it for them' feel
Nice to have
• simple, elegant, clean
Should not have
• not be too busy

```html
<!DOCTYPE html>
<html lang="en">
<head>
<meta charset="utf-8">
<title>Verdanta – Full Landscape Package</title>
<link rel="stylesheet" href="https://fonts.googleapis.com/css2?family=Open+Sans:wght@400;700&display=swap">
<style>
  :root {
    --lime: #c3d52f;
    --navy: #1d5d8f;
    --ink: #2b2b2b;
    --paper: #ffffff;
    --backdrop: #e4e6e3;
    --plate: #eceef0;
    --dusk-top: #8a7fc0;
    --dusk-mid: #b7aedb;
    --dusk-low: #5b4a6e;
  }
  * { box-sizing: border-box; margin: 0; padding: 0; }
  html, body { width: 1200px; height: 799px; overflow: hidden; }
  body {
    background: var(--backdrop);
    font-family: "Open Sans", Arial, sans-serif;
    color: var(--ink);
    position: relative;
  }
  .spread {
    position: absolute; left: 50px; top: 205px;
    width: 1100px; height: 389px;
    display: flex;
    box-shadow: 0 6px 24px rgba(0,0,0,.18);
  }
  .panel { position: relative; width: 550px; height: 389px; background: var(--paper); overflow: hidden; }
  .panel + .panel { border-left: 1px solid #e6e6e6; }
  .corner { position: absolute; width: 30px; height: 30px; background: var(--lime); }
  .corner--tr { top: 0; right: 0; }
  .corner--bl { bottom: 0; left: 0; }
  .header-band { position: absolute; left: 0; right: 0; top: 0; height: 52px; border-bottom: 2px solid var(--lime); }
  .brand {
    position: absolute; right: 42px; top: 16px;
    display: flex; align-items: center; gap: 6px;
    font-weight: 700; font-size: 13px; color: var(--navy); letter-spacing: .5px;
  }
  .brand-dot { width: 16px; height: 16px; border-radius: 50%; background: var(--navy); }
  .photo { position: absolute; left: 0; right: 0; top: 54px; bottom: 40px; }
  .photo--home { background: linear-gradient(180deg, var(--dusk-mid) 0%, #d9c9d6 35%, #6f6a85 60%, #4d5a6a 85%, #6d8a4a 100%); }
  .photo--pool { background: linear-gradient(180deg, var(--dusk-top) 0%, var(--dusk-mid) 40%, #6a5a78 70%, var(--dusk-low) 100%); bottom: 44px; border-bottom: 2px solid var(--lime); }
  .offer {
    position: absolute; left: 0; top: 54px; bottom: 40px; width: 262px;
    background: rgba(255,255,255,.9);
    text-align: center; padding: 16px 6px 0;
    font-size: 7.4px; line-height: 1.5;
    white-space: nowrap;
  }
  .member-plate { width: 110px; height: 46px; margin: 0 auto 10px; border-radius: 3px; background: var(--plate); }
  .offer-title { font-weight: 700; font-size: 8px; }
  .offer-price { font-weight: 700; color: var(--navy); }
  .offer-web { font-weight: 700; font-size: 8.6px; margin-top: 3px; }
  .cover-band {
    position: absolute; left: 0; right: 0; top: 120px; height: 120px;
    background: rgba(255,255,255,.55);
  }
  .member-plate--cover { position: absolute; left: 50%; top: 142px; transform: translateX(-50%); width: 160px; height: 70px; margin: 0; background: rgba(255,255,255,.85); }
  .cover-web { position: absolute; right: 48px; bottom: 14px; font-size: 11px; color: #555; }
</style>
</head>
<body>
  <div class="spread">
    <section class="panel panel--inside">
      <div class="header-band"></div>
      <div class="corner corner--tr"></div>
      <div class="brand"><span class="brand-dot"></span>VERDANTA</div>
      <div class="photo photo--home" role="img" aria-label="New two-storey home with garage and lawn at dusk"></div>
      <div class="offer">
        <div class="member-plate" role="img" aria-label="Industry association membership mark"></div>
        <p class="offer-title">VERDANTA – FULL LANDSCAPE PACKAGE</p>
        <p>Create your outdoor space with our landscape packages</p>
        <p>starting from <span class="offer-price">$9,990+GST</span></p>
        <p>Inclusions – Everything you need to love your outdoor space</p>
        <p>Site consultation including a measure and quote</p>
        <p>Site preparation and clearing</p>
        <p>New turf including premium soil installed to front &amp; back yards</p>
        <p>River rock to sides of house</p>
        <p>Feature garden bed</p>
        <p>Rubbish removal, clean and watering</p>
        <p>Customised options available</p>
        <p>Speak to us today to organise your free quote</p>
        <p>Visit our website for more ideas!</p>
        <p class="offer-web">www.verdantayards.com.au</p>
      </div>
      <div class="corner corner--bl"></div>
    </section>
    <section class="panel panel--cover">
      <div class="header-band"></div>
      <div class="corner corner--tr"></div>
      <div class="brand"><span class="brand-dot"></span>VERDANTA</div>
      <div class="photo photo--pool" role="img" aria-label="Modern home with lit pool and deck at twilight"></div>
      <div class="cover-band"></div>
      <div class="member-plate member-plate--cover" role="img" aria-label="Industry association membership mark"></div>
      <p class="cover-web">www.verdantayards.com.au</p>
      <div class="corner corner--bl"></div>
    </section>
  </div>
</body>
</html>
```